Courier Business needs a Business Card Design !!!

My new company needs a business card design. Our company name is Maple Dart Courier & Delivery Services. We will be servicing residential , government and business clients in the City of Yellowknife, Northwest Territories, Canada. I would like the following information included on the card: Name- Calvin Oxley. Title- Owner. Company- Maple Dart Courier & Delivery Services. Address- PO Box 5918 , Yellowknife , NWT, X0E 4K3. Phone- 867-555-0193. Email- mapledartdelivery@postfern.example. Facebook- www.socialpage.example/mapledartdelivery. I would like my double sided card to be the standard size of 84mm x 55mm. No borders. Use CMYK mode.1039x 697 pixels at least. I would like my logo to take up at least one quarter of the area of one side of the card. Text should be at least 8 point with perhaps my name being 10 point and my company name being 12-15 point . It should have clear readable font. Please use one or two bold colors. I am trying to attract the business community so a professional look might be best. My tag line is " On Time Every Time ". Nice safe margins please. We will be providing fast, reliable and professional delivery of envelopes and small packages within the City of Yellowknife. We offer 100% satisfaction or a complete refund. I have included a file of our logo. I like black, blue and red but am willing to look at what you feel would work best. I do not really like white as a background color.

Target Market(s)

Professionals , business owners. 30-50 years old

Industry/Entity Type

Residential

Contact Information for Business Card

As noted in brief

Font styles to use
Serif
Sans Serif

Colors
000000
0255a3
f04a50

Requirements
Must have
• My contact info. My logo
Nice to have
• Simple elegant design but still catches the eye
Should not have
• White background color

```html
<!DOCTYPE html>
<html lang="en">
<head>
<meta charset="utf-8">
<title>Maple Dart Courier &amp; Delivery Services – Business Card</title>
<link rel="stylesheet" href="https://fonts.googleapis.com/css2?family=Roboto+Condensed:wght@300;400;700&family=Roboto:wght@400;700&display=swap">
<style>
  :root {
    --page-bg: #ecebea;
    --brand-blue: #0255a3;
    --brand-red: #f04a50;
    --accent-green: #8dc63f;
    --paper-white: #ffffff;
    --ink-dark: #1d1d1b;
  }
  * { box-sizing: border-box; margin: 0; padding: 0; }
  html, body {
    width: 1000px; height: 1200px; overflow: hidden;
    background: var(--page-bg);
  }
  .card-spread {
    position: absolute;
    left: 40px; top: 450px;
    width: 920px; height: 301px;
    display: flex;
    box-shadow: 0 6px 18px rgba(0,0,0,0.15);
  }
  .card {
    position: relative;
    width: 460px; height: 301px;
    overflow: hidden;
  }
  .card-front { background: var(--brand-blue); }
  .card-back { background: var(--brand-red); }

  .logo-panel {
    position: absolute;
    left: 100px; top: 0;
    width: 260px; height: 139px;
    background: var(--paper-white);
    display: flex; align-items: center; justify-content: center; gap: 10px;
    padding: 0 14px;
  }
  .logo-mark {
    width: 16px; height: 16px; flex: none;
    background: var(--brand-red);
  }
  .company-name {
    font-family: "Roboto Condensed", sans-serif;
    font-weight: 700;
    font-size: 19px;
    line-height: 1.15;
    color: var(--brand-red);
    text-transform: uppercase;
  }

  .name-block {
    position: absolute;
    left: 0; right: 0; top: 194px;
    text-align: center;
    color: var(--accent-green);
    font-family: "Roboto Condensed", sans-serif;
  }
  .person-name {
    font-size: 24px;
    line-height: 1;
    text-transform: uppercase;
    letter-spacing: -0.3px;
  }
  .person-name .first { font-weight: 700; }
  .person-name .last { font-weight: 300; }
  .person-title {
    display: flex; align-items: center; justify-content: center; gap: 6px;
    font-size: 21px; font-weight: 400; line-height: 1; margin-top: -2px;
  }
  .person-title::before, .person-title::after {
    content: ""; width: 46px; height: 2px; background: var(--accent-green);
  }

  .tab-strip {
    position: absolute;
    left: 100px; bottom: 0;
    width: 260px; height: 28px;
    background: var(--paper-white);
  }

  .contact-block {
    position: absolute;
    left: 0; right: 0; top: 118px;
    text-align: center;
    color: var(--paper-white);
    font-family: "Roboto", sans-serif;
    font-size: 13.5px;
    line-height: 21px;
  }
  .contact-line {
    display: flex; align-items: center; justify-content: center; gap: 5px;
  }
  .contact-line .phone { font-weight: 700; margin-right: 4px; }
  .contact-icon {
    width: 12px; height: 12px; flex: none;
    background: var(--ink-dark); border-radius: 2px;
    display: inline-flex; align-items: center; justify-content: center;
  }
  .contact-icon svg { width: 9px; height: 9px; }
</style>
</head>
<body>
  <main class="card-spread">
    <section class="card card-front" aria-label="Card front">
      <div class="logo-panel">
        <span class="logo-mark"></span>
        <div class="company-name">Maple Dart<br>Courier &amp; Delivery Services</div>
      </div>
      <div class="name-block">
        <div class="person-name"><span class="first">Calvin</span><span class="last">Oxley</span></div>
        <div class="person-title">owner</div>
      </div>
      <div class="tab-strip"></div>
    </section>

    <section class="card card-back" aria-label="Card back">
      <div class="contact-block">
        <div class="contact-line">PO Box 5918, Yellowknife, NWT, X0E 4K3.</div>
        <div class="contact-line">
          <span class="contact-icon"><svg viewBox="0 0 24 24"><path fill="#fff" d="M6.6 10.8a15.2 15.2 0 0 0 6.6 6.6l2.2-2.2c.3-.3.7-.4 1-.2 1.1.4 2.3.6 3.6.6.6 0 1 .4 1 1V20c0 .6-.4 1-1 1A17 17 0 0 1 3 4c0-.6.4-1 1-1h3.5c.6 0 1 .4 1 1 0 1.3.2 2.5.6 3.6.1.3 0 .7-.2 1z"/></svg></span>
          <span class="phone">867-555-0193</span>
          <span class="contact-icon"><svg viewBox="0 0 24 24"><path fill="#fff" d="M2 5h20v14H2z M3.5 6.5 12 12.5l8.5-6" stroke="#1d1d1b" stroke-width="1.5"/></svg></span>
          <span>mapledartdelivery@postfern.example</span>
        </div>
        <div class="contact-line">
          <span class="contact-icon"></span>
          <span>/mapledartdelivery</span>
        </div>
      </div>
      <div class="tab-strip"></div>
    </section>
  </main>
</body>
</html>
```